Brevinor
Brevinor - Consulting
Use same font as used in my logo
It is up to you.
Simple
Lionel Brasquet
President
82 Thornwell Avenue Toronto, Ontario M4R 2J8
l.brasquet@brevinorhub.com
www.brevinorhub.com
Will be the same however in French

```html
<!DOCTYPE html>
<html lang="en">
<head>
<meta charset="utf-8">
<title>Brevinor – Business Card Set</title>
<link href="https://fonts.googleapis.com/css2?family=Arimo:wght@400;700&display=swap" rel="stylesheet">
<style>
  :root {
    --frame: #111111;
    --sheet-light: #ececec;
    --sheet-dark: #cfcfcf;
    --card-edge: #8d8d8d;
    --brand-blue: #2c5c8f;
    --brand-blue-deep: #0f3766;
    --swoosh-grey: #6e6e6e;
    --charcoal-light: #6a6a6a;
    --charcoal-dark: #4a4a4a;
    --white: #ffffff;
  }
  * { box-sizing: border-box; margin: 0; padding: 0; }
  html, body {
    width: 1200px; height: 670px; overflow: hidden;
    background: var(--frame);
    font-family: "Arimo", Arial, sans-serif;
  }
  .sheet {
    position: absolute; left: 10px; top: 10px; width: 1180px; height: 650px;
    background: radial-gradient(ellipse at 50% 40%, var(--sheet-light), var(--sheet-dark));
  }
  .card {
    position: absolute; width: 482px; height: 274px;
    border: 2px solid var(--card-edge); border-radius: 24px; overflow: hidden;
  }
  .card--front { left: 76px; top: 28px; background: var(--white); }
  .card--back-blue { left: 595px; top: 28px;
    background: linear-gradient(100deg, var(--brand-blue-deep), var(--brand-blue)); }
  .card--back-white { left: 76px; top: 331px; background: var(--white); }
  .card--back-grey { left: 595px; top: 331px;
    background: linear-gradient(100deg, var(--charcoal-dark), var(--charcoal-light)); }

  .wordmark {
    display: flex; align-items: center; gap: 10px;
    font-weight: 700; letter-spacing: 3px; text-transform: uppercase;
  }
  .wordmark__dot { width: 14px; height: 14px; border-radius: 50%; background: currentColor; }
  .wordmark--small { position: absolute; left: 26px; top: 28px; font-size: 22px; color: var(--brand-blue); }
  .wordmark--large {
    position: absolute; left: 0; right: 0; top: 50%; transform: translateY(-50%);
    justify-content: center; font-size: 38px;
  }
  .wordmark--on-dark { color: var(--white); }
  .wordmark--on-light { color: var(--brand-blue); }

  .holder { position: absolute; left: 200px; width: 220px; top: 90px; text-align: center; }
  .holder__name { font-size: 22px; font-weight: 700; color: var(--brand-blue); }
  .holder__title { font-size: 13px; color: var(--brand-blue); margin-top: 4px; }

  .front-band { position: absolute; left: 0; bottom: 0; width: 482px; height: 130px; }
  .contact {
    position: absolute; left: 14px; top: 180px;
    font-size: 12.5px; line-height: 15.5px; color: var(--white);
  }
</style>
</head>
<body>
<div class="sheet">

  <section class="card card--front">
    <div class="wordmark wordmark--small"><span class="wordmark__dot"></span>Brevinor</div>
    <div class="holder">
      <p class="holder__name">Lionel Brasquet</p>
      <p class="holder__title">President</p>
    </div>
    <svg class="front-band" viewBox="0 0 482 130" preserveAspectRatio="none" aria-hidden="true">
      <defs>
        <linearGradient id="bandFill" x1="0" y1="0" x2="1" y2="0">
          <stop offset="0" stop-color="#1e4877"/>
          <stop offset="1" stop-color="#2f6196"/>
        </linearGradient>
      </defs>
      <path d="M0 10 C120 -6 300 2 482 34 L482 48 C300 16 120 10 0 26 Z" fill="var(--swoosh-grey)"/>
      <path d="M0 28 C120 12 300 18 482 50 L482 130 L0 130 Z" fill="url(#bandFill)"/>
    </svg>
    <address class="contact" style="font-style:normal">
      82 Thornwell Avenue<br>
      Toronto, Ontario, M4R 2J8<br>
      Cell: (416) 555-0184<br>
      Email: l.brasquet@brevinorhub.com<br>
      www.brevinorhub.com
    </address>
  </section>

  <section class="card card--back-blue">
    <div class="wordmark wordmark--large wordmark--on-dark"><span class="wordmark__dot"></span>Brevinor</div>
  </section>

  <section class="card card--back-white">
    <div class="wordmark wordmark--large wordmark--on-light"><span class="wordmark__dot"></span>Brevinor</div>
  </section>

  <section class="card card--back-grey">
    <div class="wordmark wordmark--large wordmark--on-dark"><span class="wordmark__dot"></span>Brevinor</div>
  </section>

</div>
</body>
</html>
```